Stone Over Tide - Stationery Design Project

Hi everyone,

We need a business card and a stationary set designed for a new corporate video production company based in Sydney, 'Stone Over Tide'.

The name refers to the mythological 'phoenix' so we would like to see designs that are appropriate to both the name and to a creative film company. The key thing is, we need to appear fresh and creative while maintaining professionalism.

We would like to stick with dark colors for the basis of the card. One idea that came up was obsidian/volcanic rock with the logo cracking through to reveal lava or something fire like. This is just one idea that has come up, but we are of course open to others and would love to see what people can come up with. Extensive use of flames/fire imagery is not really what we are after.

Also, cinematic as opposed to corporate is preferable.

**** UPDATE ****
When I hand over the card to a prospective client, I want them to feel like they are receiving an obsidian plate with inscriptions in it (ie the phoenix). Looking for something elemental and rigid to contrast and complement the graceful lines of the logo.

Designs we require:
- Business card
(We would like a business card that makes use of some of the more premium business card printing options, such as foil stamping, embossing/debossing, painted edges, spot UV etc. Doesnt have to use all these things, only what you feel works, but we are looking for a business card that stands out and is memorable and these nice touches have that effect. For an example of what is possible, check out "http://www.velvetprintery.net/base/category/business-card-gallery/".)

- Letter head
- With compliments slip
- Display folder

COPMPANY DETAILS:
ABN: 62 738 294 019
Company Address: 7/18-20 Kell St, Marbury NSW 2058
Name: Rex M. Dunleavy
Title: Producer
Contact Number: 0412 539 204
email: rex@stoneovertide.com
website: www.stoneovertide.com

ABOUT THE PHOENIX:
The phoenix is a musical bird from mythology, known for its long fancy tail and small plume on the top of its head. They are elegant and graceful and symbolize immortality, endurance and strength, believed to live for 5 centuries before they were reborn from their ashes.
Updates

Hi everyone,

We have just updated the design brief to include business contact information, website etc. should anyone require it for their designs.

Thanks

Rex

Target Market(s)

Other creative businesses and marketing firms.

Industry/Entity Type

Printing

Requirements
Must have
• Basic printing requirements:
- CMYK colour space
- 300dpi resolution
- Color bleed/crop marks etc to allow for trimming where necessary
- Source files upon handover
Should not have
• Overuse of fire/flame imagery

```html
<!DOCTYPE html>
<html lang="en">
<head>
<meta charset="utf-8">
<title>Stone Over Tide — Stationery Set</title>
<link href="https://fonts.googleapis.com/css2?family=Open+Sans:wght@400;600&display=swap" rel="stylesheet">
<style>
  :root {
    --backdrop: #ececec;
    --paper: #ffffff;
    --paper-edge: #dcdcdc;
    --ember: #d8342c;
    --folder-top: #dc5a30;
    --folder-bottom: #c2282a;
    --ink: #3a3a3a;
    --rule: #9a9a9a;
    --card-dark: #151515;
  }
  html, body {
    margin: 0;
    width: 1200px;
    height: 794px;
    overflow: hidden;
    background: var(--backdrop);
    font-family: "Open Sans", Arial, sans-serif;
  }
  .set { position: relative; width: 1200px; height: 794px; }
  .sheet {
    position: absolute;
    background: var(--paper);
    border: 1px solid var(--paper-edge);
    box-sizing: border-box;
    overflow: hidden;
  }

  .wordmark {
    position: absolute;
    display: flex;
    align-items: center;
    gap: 7px;
    color: var(--ember);
    font-weight: 400;
    text-transform: uppercase;
    white-space: nowrap;
  }
  .wordmark .mark-dot {
    width: 14px; height: 14px;
    border-radius: 50%;
    background: var(--ember);
    flex: none;
  }

  .contact {
    position: absolute;
    border-left: 1px solid var(--rule);
    padding-left: 5px;
    font-size: 4.2px;
    line-height: 5.6px;
    font-style: normal;
    color: var(--ink);
    white-space: nowrap;
  }
  .contact ul { margin: 0; padding: 0; }
  .contact li { list-style: none; display: flex; align-items: center; gap: 3px; }
  .contact .icon { width: 3px; height: 3px; background: var(--ember); flex: none; }
  .contact .icon.blank { background: none; }

  /* Letterhead */
  .letterhead { left: 292px; top: 98px; width: 293px; height: 415px; }
  .letterhead .wordmark { left: 14px; top: 26px; font-size: 7px; letter-spacing: 3.2px; }
  .letterhead .contact { left: 225px; top: 16px; }

  /* Folder */
  .folder {
    position: absolute;
    left: 636px; top: 80px; width: 346px; height: 436px;
    background: linear-gradient(180deg, var(--folder-top), var(--folder-bottom));
  }
  .folder-band {
    position: absolute;
    left: 0; top: 118px; width: 340px; height: 57px;
    background: var(--paper);
    border-radius: 0 30px 30px 0;
  }
  .folder-band .wordmark { left: 96px; top: 21px; font-size: 8px; letter-spacing: 3.6px; }
  .folder-url {
    position: absolute; right: 12px; bottom: 14px;
    color: #fff; font-size: 8px;
  }

  /* Business cards */
  .card-front { left: 186px; top: 550px; width: 133px; height: 75px; }
  .card-front .wordmark { left: 8px; top: 12px; }
  .card-front .wordmark .mark-dot { width: 18px; height: 18px; }
  .card-name {
    position: absolute; right: 7px; top: 7px; text-align: right;
    font-size: 7.5px; line-height: 9px; color: var(--ink);
  }
  .card-name .role { display: block; font-size: 4.5px; line-height: 6px; color: var(--ember); }
  .card-front .contact { left: 70px; top: 32px; font-size: 3.6px; line-height: 5px; }

  .card-back {
    position: absolute; left: 186px; top: 646px; width: 133px; height: 75px;
    background: var(--card-dark);
  }
  .card-back .mark-dot {
    position: absolute; left: 56px; top: 14px; width: 20px; height: 20px;
    border-radius: 50%; background: var(--ember);
  }
  .card-back .wordmark {
    left: 0; right: 0; top: 53px; justify-content: center;
    color: #fff; font-size: 5.6px; letter-spacing: 2.4px;
  }
  .card-back .card-url {
    position: absolute; left: 0; right: 0; top: 65px; text-align: center;
    color: #bbb; font-size: 3.5px;
  }

  /* Compliment slips */
  .slip { width: 328px; height: 158px; }
  .slip-plain { left: 353px; top: 560px; }
  .slip-flap { left: 713px; top: 562px; }
  .slip .wordmark { left: 14px; top: 30px; font-size: 6.6px; letter-spacing: 3px; }
  .slip .contact { left: 262px; top: 18px; }
  .flap-line {
    position: absolute; left: 0; right: 0; top: 62px;
    border-top: 1px solid #e4e4e4;
  }
  .compliments {
    position: absolute; left: 20px; top: 103px; margin: 0;
    color: var(--ember); font-size: 11.5px; font-weight: 400;
  }
</style>
</head>
<body>
<main class="set">

  <section class="sheet letterhead" aria-label="Letterhead">
    <div class="wordmark"><span class="mark-dot"></span>Stone Over Tide</div>
    <address class="contact">
      <ul>
        <li><span class="icon"></span>7/18-20 Kell St</li>
        <li><span class="icon blank"></span>Marbury NSW 2058</li>
        <li><span class="icon"></span>0412 539 204</li>
        <li><span class="icon"></span>02 8731 4460</li>
        <li><span class="icon"></span>02 8731 4461</li>
        <li><span class="icon"></span>rex@stoneovertide.com</li>
        <li><span class="icon"></span>www.stoneovertide.com</li>
      </ul>
    </address>
  </section>

  <section class="folder" aria-label="Display folder">
    <div class="folder-band">
      <div class="wordmark"><span class="mark-dot"></span>Stone Over Tide</div>
    </div>
    <div class="folder-url">www.stoneovertide.com</div>
  </section>

  <section class="sheet card-front" aria-label="Business card front">
    <div class="wordmark"><span class="mark-dot"></span></div>
    <div class="card-name">Rex M. Dunleavy<span class="role">Producer</span></div>
    <address class="contact">
      <ul>
        <li><span class="icon"></span>7/18-20 Kell St</li>
        <li><span class="icon blank"></span>Marbury NSW 2058</li>
        <li><span class="icon"></span>0412 539 204</li>
        <li><span class="icon"></span>02 8731 4460</li>
        <li><span class="icon"></span>rex@stoneovertide.com</li>
      </ul>
    </address>
  </section>

  <section class="card-back" aria-label="Business card back">
    <span class="mark-dot"></span>
    <div class="wordmark">Stone Over Tide</div>
    <div class="card-url">www.stoneovertide.com</div>
  </section>

  <section class="sheet slip slip-plain" aria-label="Compliments slip">
    <div class="wordmark"><span class="mark-dot"></span>Stone Over Tide</div>
    <address class="contact">
      <ul>
        <li><span class="icon"></span>7/18-20 Kell St</li>
        <li><span class="icon blank"></span>Marbury NSW 2058</li>
        <li><span class="icon"></span>0412 539 204</li>
        <li><span class="icon"></span>02 8731 4460</li>
        <li><span class="icon"></span>02 8731 4461</li>
        <li><span class="icon"></span>rex@stoneovertide.com</li>
        <li><span class="icon"></span>www.stoneovertide.com</li>
      </ul>
    </address>
  </section>

  <section class="sheet slip slip-flap" aria-label="With compliments slip">
    <div class="flap-line"></div>
    <div class="wordmark"><span class="mark-dot"></span>Stone Over Tide</div>
    <address class="contact">
      <ul>
        <li><span class="icon"></span>7/18-20 Kell St</li>
        <li><span class="icon blank"></span>Marbury NSW 2058</li>
        <li><span class="icon"></span>0412 539 204</li>
        <li><span class="icon"></span>02 8731 4460</li>
        <li><span class="icon"></span>02 8731 4461</li>
        <li><span class="icon"></span>rex@stoneovertide.com</li>
        <li><span class="icon"></span>www.stoneovertide.com</li>
      </ul>
    </address>
    <p class="compliments">With Compliments</p>
  </section>

</main>
</body>
</html>
```